Brindle's Coating & Renewal Letterhead Design We want to revamp out old traditional letterhead with the new logo designs that are attached. We are working on getting all our company items from vehicles, business, cards, t-shirts, letterhead to match. This should include company colors, fonts, and flow of items that we have attached below.

Industry/Entity Type

Construction Company

Font styles to use
Sans Serif
Other font styles liked:
• Bold with outline

Colors
ec1f27
ffffff

Requirements
Must have
• Company Name: Brindle's Coating & Renewal
• Address: 4172 SW 83rd Ter Harrow Cove fl 30418
• Office Number: (555) 240-6193
• Email: brindlesrenewal@mailnest-example.com
• License Number: QRT8046392
Nice to have
• Company Colors: red, white, black, and grey

```html
<!DOCTYPE html>
<html lang="en">
<head>
<meta charset="utf-8">
<title>Brindle's Coating &amp; Renewal Letterhead</title>
<link href="https://fonts.googleapis.com/css2?family=Poppins:wght@300;400;500;700&display=swap" rel="stylesheet">
<style>
  :root{
    --brand-red:#e43d17;
    --ink:#1d1d1d;
    --muted:#7a7a7a;
    --rule:#c9c9c9;
    --paper:#fafbfc;
    --backdrop:#5b5b5b;
  }
  *{margin:0;padding:0;box-sizing:border-box}
  html,body{width:1200px;height:909px;overflow:hidden;background:var(--backdrop);font-family:"Poppins",sans-serif;color:var(--ink)}
  .letterhead{position:absolute;left:267px;top:24px;width:665px;height:860px;background:var(--paper);overflow:hidden}
  .corner-texture{position:absolute;right:0;top:0;width:160px;height:175px;
    background:linear-gradient(225deg,#d9d9d9 0%,#ececec 40%,rgba(250,251,252,0) 75%)}
  .brand{position:absolute;left:30px;top:40px;width:200px;color:var(--brand-red);font-weight:700;font-size:22px;line-height:1.1;letter-spacing:.3px}
  .years-badge{position:absolute;right:22px;top:42px;width:52px;height:52px;border:3px solid var(--brand-red);border-radius:50%}
  .sender{position:absolute;left:38px;top:130px;font-size:8.5px;line-height:14px}
  .sender .name{color:var(--brand-red);font-size:10.5px;line-height:14px}
  .sender .role{color:var(--muted);font-size:6.5px;line-height:8px;margin-bottom:9px}
  .sender b{color:var(--brand-red);font-weight:500}
  .body-copy{position:absolute;left:30px;top:260px;width:620px;font-size:9.6px;line-height:14.2px}
  .body-copy p{margin-bottom:14px}
  .signature{position:absolute;left:31px;top:640px;width:120px;height:34px;background:linear-gradient(90deg,#e4e4e4,#f1f1f1)}
  .signer{position:absolute;left:32px;top:682px}
  .signer .name{font-size:13px;font-weight:300;color:#333}
  .signer .role{font-size:7px;color:var(--muted)}
  .footer-rule{position:absolute;left:30px;top:762px;width:623px;height:2px;background:var(--rule)}
  .footer-rule::before{content:"";position:absolute;left:0;top:0;width:87px;height:2px;background:var(--brand-red)}
  .contact{position:absolute;top:779px;display:flex;align-items:center;gap:9px;font-size:8.8px;line-height:12.5px}
  .contact svg{width:20px;height:20px;flex:none}
  .contact.address{left:34px}
  .contact.reach{left:270px}
  .contact.license{left:522px}
  .bottom-band{position:absolute;left:0;bottom:0;width:100%;height:18px;background:var(--brand-red)}
</style>
</head>
<body>
<main class="letterhead">
  <div class="corner-texture" role="img" aria-label="Faint grey diamond pattern fading from the top-right corner"></div>
  <div class="brand">Brindle's Coating &amp; Renewal</div>
  <div class="years-badge" role="img" aria-label="Family owned and operated anniversary badge"></div>

  <div class="sender">
    <div class="name">Marla Quentin</div>
    <div class="role">Chief Director</div>
    <div><b>A:</b> 22/7 Elm Rd, FL.4106</div>
    <div><b>E:</b> info@marla.quentin-example.com</div>
    <div><b>P:</b> +9155502 71846</div>
  </div>

  <section class="body-copy">
    <p>Lorem ipsum dolor sit amet, consectetur adipiscing elit. Mauris dignissim ante et magna iaculis auctor. Donec euismod eros at lectus dictum ultricies. Vivamus pulvinar commodo lectus, vel ullamcorper ligula auctor non. Fusce diam purus, aliquet at bibendum in, consequat ut neque.</p>
    <p>Praesent convallis risus ac orci maximus mollis. Phasellus eget velit efficitur, consequat nisi a, rhoncus mi. Nulla facilisi. Cras efficitur ultrices urna, porttitor accumsan justo bibendum nec. Suspendisse pellentesque imperdiet mi vel pharetra. Lorem ipsum dolor sit amet, consectetur adipiscing elit.</p>
    <p>Suspendisse dictum nulla commodo, suscipit nunc nec, auctor ante. Pellentesque libero diam, congue quis gravida ut, egestas at dui. Mauris diam lacus, euismod eget cursus in, accumsan sit amet dolor. Curabitur lobortis nibh eget augue bibendum varius. Mauris sodales bibendum lacus. iquam suscipit, nulla sed scelerisque ultrices, arcu tortor finibus arcu, nec cursus neque turpis sed risus. Mauris enim nibh, luctus at volutpat vitae, vulputate ut ipsum. Etiam commodo tempor massa, id tempor metus pretium nec.</p>
    <p>Nunc at nisi malesuada, pellentesque arcu vel, ultricies eros. Suspendisse vel magna erat. Nunc erat augue, finibus vel dapibus eu, interdum non nunc. Nullam accumsan rutrum neque, ut efficitur leo molestie eget. Fusce feugiat varius varius.</p>
    <p>Donec sit amet laoreet urna. Vivamus sem tellus, blandit at viverra ac, rhoncus id arcu. Nullam tincidunt velit nulla, sit amet laoreet enim commodo consectetur. Phasellus a erat quis ante aliquam ullamcorper. Etiam hendrerit mollis leo, in tincidunt enim euismod vel. Vestibulum imperdiet odio orci, et luctus neque rhoncus sed.</p>
  </section>

  <div class="signature" role="img" aria-label="Handwritten signature"></div>
  <div class="signer">
    <div class="name">Dorian Vale</div>
    <div class="role">Manager</div>
  </div>

  <div class="footer-rule"></div>

  <div class="contact address">
    <svg viewBox="0 0 20 20" fill="none" stroke="var(--brand-red)" stroke-width="1.5"><path d="M10 18s-6-6-6-10a6 6 0 0 1 12 0c0 4-6 10-6 10z"/><circle cx="10" cy="8" r="2.3"/></svg>
    <div>4172 SW 83rd Ter,<br>Harrow Cove, Fl 30418</div>
  </div>
  <div class="contact reach">
    <svg viewBox="0 0 20 20" fill="none" stroke="var(--brand-red)" stroke-width="1.3"><rect x="3" y="3" width="10" height="12" rx="1"/><path d="M5 6h6M5 9h6"/><rect x="9" y="10" width="9" height="7" rx="1"/><path d="M9 10l4.5 4 4.5-4"/></svg>
    <div>(555) 240-6193<br>brindlesrenewal@mailnest-example.com</div>
  </div>
  <div class="contact license">
    <svg viewBox="0 0 20 20" fill="none" stroke="var(--brand-red)" stroke-width="1.3"><rect x="2" y="5" width="16" height="11" rx="1"/><circle cx="10" cy="10.5" r="2.5"/><path d="M5 3h10M4 8h2M14 8h2"/></svg>
    <div>License Number<br>QRT8046392</div>
  </div>

  <div class="bottom-band"></div>
</main>
</body>
</html>
```